i need a US celebrity blog design

hi, i need a blog which have US celebrity news. My blog should be attractive and mature with a good theme. Readers of my blog should be able to comment. You can include any attractive colour (blue, green, purple, red).

Target Market(s)

Celebrity fans and enthusiasts

Industry/Entity Type

News

```html
<!DOCTYPE html>
<html lang="en">
<head>
<meta charset="utf-8">
<title>Mustreads – Celebrity News Blog</title>
<link href="https://fonts.googleapis.com/css2?family=Open+Sans:wght@300;400;600;700&display=swap" rel="stylesheet">
<style>
:root{
  --brand:#d7000f;
  --brand-dark:#b3000c;
  --ink:#111;
  --text:#555;
  --muted:#8a8a8a;
  --rule:#e2e2e2;
  --page:#fbfbfb;
  --white:#fff;
}
*{box-sizing:border-box;margin:0;padding:0}
html,body{width:737px;height:1200px;overflow:hidden}
body{position:relative;background:var(--page);font-family:'Open Sans',Arial,sans-serif;color:var(--text)}
.abs{position:absolute}
a{color:inherit;text-decoration:none}

/* header */
.site-header{position:absolute;left:0;top:0;width:737px;height:60px;background:var(--brand)}
.account-links{position:absolute;top:11px;left:515px;font-size:6px;color:var(--white);display:flex;gap:21px}
.main-nav{position:absolute;top:41px;left:123px;font-size:9.5px;font-weight:700;color:var(--white)}
.main-nav a{position:absolute;white-space:nowrap}
.header-search{position:absolute;left:520px;top:41px;width:76px;height:12px;background:var(--white);border-radius:1px}
.header-search-icon{position:absolute;left:599px;top:41px}

/* media placeholders */
.media{position:absolute;display:block}

/* type */
.kicker{position:absolute;font-size:5px;text-transform:uppercase;color:#555}
.headline-lg{position:absolute;font-size:12.5px;font-weight:700;line-height:16.5px;color:var(--brand)}
.headline-lg.dark{color:var(--ink)}
.headline-sm{position:absolute;font-size:8px;font-weight:700;line-height:9.5px;color:var(--ink)}
.headline-sm.narrow{font-size:7.2px;line-height:9px;white-space:nowrap;letter-spacing:-0.05px}
.excerpt-lg{position:absolute;font-size:7.6px;line-height:13px;color:#666}
.excerpt-sm{position:absolute;font-size:5.6px;line-height:7.8px;color:#777}
.byline{position:absolute;font-size:5.5px;color:#555;white-space:nowrap}
.byline b{font-weight:700}
.byline .sep{margin:0 4px;color:#aaa}
.stats{position:absolute;display:flex;gap:5px}
.stats span{display:flex;align-items:center;gap:2px;height:11px;padding:0 4px;border:1px solid #ececec;border-radius:5px;background:var(--white);font-size:4.5px;color:#c4c4c4}
.rule{position:absolute;height:1px;background:var(--rule)}
.vrule{position:absolute;width:1px;background:var(--rule)}
.section-title{position:absolute;font-size:9px;font-weight:400;color:var(--brand);text-transform:uppercase}

/* sidebar */
.mini-item{position:absolute;font-size:5.6px;line-height:7.8px;color:var(--ink);font-weight:600}
.mini-item time{display:block;font-weight:400;color:var(--muted)}
.widget-label{position:absolute;font-size:9.5px;font-weight:300;color:#888}
.field{position:absolute;background:var(--white);border:1px solid #ddd;border-radius:3px;font-size:5.5px;color:#bbb;padding:6px 5px 0}
.search-btn{position:absolute;background:var(--brand);border-radius:0 3px 3px 0}
.popular-title{position:absolute;font-size:9px;font-weight:700;color:var(--brand)}
.popular-item{position:absolute;left:487px;width:127px;font-size:5.8px;line-height:9px;color:#333;padding-left:8px}
.popular-item b{position:absolute;left:0;top:0;color:var(--brand);font-size:7px}
.follow-box{position:absolute;left:487px;top:526px;width:127px;height:64px;background:var(--brand);border-radius:4px}
.follow-box h3{position:absolute;left:8px;top:6px;font-size:12px;font-weight:700;color:var(--white)}
.social{position:absolute;display:flex;gap:6px;font-size:5.5px;color:var(--white);font-weight:600}
.social span{display:flex;flex-direction:column;align-items:center;gap:2px}
.social i{display:block;width:16px;height:16px;border-radius:3px;background:var(--white);opacity:.9}
.categories-title{position:absolute;font-size:9.5px;font-weight:700;color:var(--ink)}
.category{position:absolute;left:489px;width:125px;font-size:5.8px;color:#333;text-transform:uppercase}
.category em{font-style:normal;color:var(--muted);margin-left:5px}
.newsletter-note{position:absolute;font-size:6px;color:#666}
.subscribe{position:absolute;left:524px;top:977px;width:53px;height:13px;background:var(--brand);border-radius:3px;color:var(--white);font-size:6px;font-weight:700;text-align:center;line-height:13px}

/* footer */
.site-footer{position:absolute;left:0;top:1156px;width:737px;height:44px;background:var(--brand);color:var(--white)}
.footer-about{position:absolute;left:120px;top:5px;width:128px;font-size:5.5px;line-height:8.5px;text-align:center}
.footer-links{position:absolute;left:300px;top:5px;width:140px;font-size:5.5px;line-height:9.5px;text-align:center}
.footer-links small{display:block;font-size:5px;color:#f3b3b7}
.footer-follow{position:absolute;left:513px;top:5px;font-size:6.5px;font-weight:700}
.footer-social{position:absolute;left:514px;top:16px;display:flex;gap:8px;font-size:4.5px;font-weight:600}
.footer-social span{display:flex;flex-direction:column;align-items:center;gap:1px}
.footer-social i{display:block;width:14px;height:14px;border-radius:2px;background:var(--white);opacity:.9}
</style>
</head>
<body>

<svg width="0" height="0" style="position:absolute">
  <defs>
    <symbol id="i-like" viewBox="0 0 10 10"><path d="M1 4h2v5H1zM4 4l2-3c1 0 1 1 1 2v1h2l-1 5H4z" fill="#cfcfcf"/></symbol>
    <symbol id="i-view" viewBox="0 0 10 10"><path d="M0 5c2-3 8-3 10 0-2 3-8 3-10 0z" fill="#cfcfcf"/><circle cx="5" cy="5" r="1.6" fill="#fff"/></symbol>
    <symbol id="i-comment" viewBox="0 0 10 10"><path d="M1 1h8v6H4L2 9V7H1z" fill="#cfcfcf"/></symbol>
  </defs>
</svg>

<header class="site-header">
  <nav class="account-links"><a>Login</a><a>Become a member</a></nav>
  <nav class="main-nav">
    <a style="left:0">Mustreads</a>
    <a style="left:72px">Cine</a>
    <a style="left:117px">Music</a>
    <a style="left:168px">Entertainment</a>
    <a style="left:257px">Social Media</a>
    <a style="left:337px">Features</a>
  </nav>
  <div class="header-search"></div>
  <svg class="header-search-icon" width="11" height="11" viewBox="0 0 11 11"><circle cx="4.5" cy="4.5" r="3" fill="none" stroke="#fff" stroke-width="1.6"/><path d="M6.8 6.8l3 3" stroke="#fff" stroke-width="2"/></svg>
</header>

<main>
  <!-- lead story -->
  <div class="media" role="img" aria-label="Cast photo of a fantasy drama in costume" style="left:123px;top:73px;width:234px;height:155px;background:linear-gradient(135deg,#2b2f33,#5a5148 55%,#1c1f22)"></div>
  <span class="kicker" style="left:123px;top:237px">Mustreads</span>
  <h1 class="headline-lg" style="left:123px;top:248px;width:240px">Lorem ipsum dolor sit amet, consectetur adipiscing elit. Fusce lorem metus.</h1>
  <p class="excerpt-lg" style="left:123px;top:299px;width:236px">Donec iaculis maximus enim et tempor. Nullam bibendum quis nibh quis ullamcorper. Sed vehicula mollis elit at ultricies. Curabitur ligula ligula, faucibus vel pretium eget, aliquet eu orci. Proin sed efficitur orci.</p>
  <p class="byline" style="left:123px;top:356px">By<span class="sep">|</span><b>February 26, 2015</b><span class="sep">|</span><b>Comments</b></p>
  <div class="stats" style="left:123px;top:376px"><span><svg width="6" height="6"><use href="#i-like"/></svg>62</span><span><svg width="7" height="6"><use href="#i-view"/></svg>95</span><span><svg width="7" height="6"><use href="#i-comment"/></svg>12</span></div>

  <div class="media" role="img" aria-label="Portrait of a long-haired music performer" style="left:369px;top:73px;width:107px;height:72px;background:linear-gradient(160deg,#cfc8c4,#8a6450 55%,#c9c2bd)"></div>
  <span class="kicker" style="left:369px;top:149px">Music</span>
  <h2 class="headline-sm narrow" style="left:369px;top:155px">Lorem ipsum dolor sit amet,<br>consectetur adipiscing elit.<br>Fusce lorem metus.</h2>
  <p class="excerpt-sm" style="left:369px;top:184px;width:106px">Donec iaculis maximus enim et tempor. Nullam bibendum quis nibh quis ullamcorper.</p>
  <div class="stats" style="left:369px;top:213px"><span><svg width="6" height="6"><use href="#i-like"/></svg>62</span><span><svg width="7" height="6"><use href="#i-view"/></svg>95</span><span><svg width="7" height="6"><use href="#i-comment"/></svg>12</span></div>

  <div class="media" role="img" aria-label="Dark film poster emblem for an upcoming superhero movie" style="left:369px;top:236px;width:107px;height:70px;background:radial-gradient(circle at 50% 45%,#7a2a2a,#2a2c30 55%,#0d0e10)"></div>
  <span class="kicker" style="left:369px;top:312px">Cine</span>
  <h2 class="headline-sm narrow" style="left:369px;top:318px">Lorem ipsum dolor sit amet,<br>consectetur adipiscing elit.<br>Fusce lorem metus.</h2>
  <p class="excerpt-sm" style="left:369px;top:347px;width:106px">Donec iaculis maximus enim et tempor. Nullam bibendum quis nibh quis ullamcorper.</p>
  <div class="stats" style="left:369px;top:376px"><span><svg width="6" height="6"><use href="#i-like"/></svg>62</span><span><svg width="7" height="6"><use href="#i-view"/></svg>95</span><span><svg width="7" height="6"><use href="#i-comment"/></svg>12</span></div>

  <div class="rule" style="left:123px;top:401px;width:354px"></div>

  <!-- second row -->
  <div class="media" role="img" aria-label="Couple sharing a moment at a red carpet event" style="left:123px;top:411px;width:170px;height:112px;background:linear-gradient(120deg,#c9a98f,#2a2524 55%,#6b5a50)"></div>
  <span class="kicker" style="left:123px;top:531px">Mustreads</span>
  <h2 class="headline-sm" style="left:123px;top:540px;width:172px">Lorem ipsum dolor sit amet, consec tetur adipiscing elit. Fusce lorem metus.</h2>
  <p class="excerpt-sm" style="left:123px;top:562px;width:172px">Donec iaculis maximus enim et tempor. Nullam bibendum quis nibh quis ullamcorper. Sed vehicula mollis elit at ultricies.</p>
  <p class="byline" style="left:123px;top:581px">By<span class="sep">|</span><b>February 26, 2015</b><span class="sep">|</span><b>Comments</b></p>
  <div class="stats" style="left:123px;top:598px"><span><svg width="6" height="6"><use href="#i-like"/></svg>62</span><span><svg width="7" height="6"><use href="#i-view"/></svg>95</span><span><svg width="7" height="6"><use href="#i-comment"/></svg>12</span></div>

  <div class="media" role="img" aria-label="Actor in a suit talking on a phone outdoors" style="left:305px;top:411px;width:171px;height:112px;background:linear-gradient(120deg,#8e8a86,#3f4248 55%,#b7aca2)"></div>
  <span class="kicker" style="left:305px;top:531px">Cine</span>
  <h2 class="headline-sm" style="left:305px;top:540px;width:172px">Lorem ipsum dolor sit amet, consec tetur adipiscing elit. Fusce lorem metus.</h2>
  <p class="excerpt-sm" style="left:305px;top:562px;width:172px">Donec iaculis maximus enim et tempor. Nullam bibendum quis nibh quis ullamcorper. Sed vehicula mollis elit at ultricies.</p>
  <p class="byline" style="left:305px;top:581px">By<span class="sep">|</span><b>February 26, 2015</b><span class="sep">|</span><b>Comments</b></p>
  <div class="stats" style="left:305px;top:598px"><span><svg width="6" height="6"><use href="#i-like"/></svg>62</span><span><svg width="7" height="6"><use href="#i-view"/></svg>95</span><span><svg width="7" height="6"><use href="#i-comment"/></svg>12</span></div>

  <div class="rule" style="left:123px;top:621px;width:354px"></div>

  <!-- editors picks -->
  <h3 class="section-title" style="left:123px;top:629px">Editors Picks</h3>
  <div class="media" role="img" aria-label="Portrait of a singer with dark styled hair" style="left:123px;top:646px;width:117px;height:77px;background:linear-gradient(120deg,#ddd6d3,#4a3a38 50%,#a33a3a)"></div>
  <h2 class="headline-sm" style="left:245px;top:645px;width:232px">Lorem ipsum dolor sit amet, consec tetur adipiscing elit. Fusce lorem metus.</h2>
  <p class="excerpt-sm" style="left:245px;top:666px;width:232px">Donec iaculis maximus enim et tempor. Nullam bibendum quis nibh quis ullamcorper. Sed vehicula mollis elit at ultricies. Curabitur ligula ligula, faucibus vel pretium eget, aliquet eu orci. Proin sed efficitur orci.</p>
  <p class="byline" style="left:245px;top:694px">By<span class="sep">|</span><b>February 26, 2015</b><span class="sep">|</span><b>Comments</b></p>
  <div class="stats" style="left:245px;top:711px"><span><svg width="6" height="6"><use href="#i-like"/></svg>62</span><span><svg width="7" height="6"><use href="#i-view"/></svg>95</span><span><svg width="7" height="6"><use href="#i-comment"/></svg>12</span></div>

  <div class="media" role="img" aria-label="Dark film poster emblem for an upcoming superhero movie" style="left:123px;top:743px;width:117px;height:79px;background:radial-gradient(circle at 50% 45%,#7a2a2a,#2a2c30 55%,#0d0e10)"></div>
  <h2 class="headline-sm" style="left:245px;top:743px;width:232px">Lorem ipsum dolor sit amet, consec tetur adipiscing elit. Fusce lorem metus.</h2>
  <p class="excerpt-sm" style="left:245px;top:764px;width:232px">Donec iaculis maximus enim et tempor. Nullam bibendum quis nibh quis ullamcorper. Sed vehicula mollis elit at ultricies. Curabitur ligula ligula, faucibus vel pretium eget, aliquet eu orci. Proin sed efficitur orci.</p>
  <p class="byline" style="left:245px;top:792px">By<span class="sep">|</span><b>February 26, 2015</b><span class="sep">|</span><b>Comments</b></p>
  <div class="stats" style="left:245px;top:808px"><span><svg width="6" height="6"><use href="#i-like"/></svg>62</span><span><svg width="7" height="6"><use href="#i-view"/></svg>95</span><span><svg width="7" height="6"><use href="#i-comment"/></svg>12</span></div>

  <div class="rule" style="left:120px;top:833px;width:362px"></div>
  <div class="vrule" style="left:341px;top:833px;height:323px"></div>

  <!-- bottom feature -->
  <div class="media" role="img" aria-label="Actresses in black gowns at an awards ceremony" style="left:123px;top:847px;width:211px;height:140px;background:linear-gradient(135deg,#c8b79a,#2a2626 50%,#8d8476)"></div>
  <span class="kicker" style="left:123px;top:993px">Mustreads</span>
  <h2 class="headline-lg dark" style="left:123px;top:1001px;width:212px">Lorem ipsum dolor sit amet, consectetur adipiscing elit. Fusce lorem metus.</h2>
  <p class="excerpt-lg" style="left:123px;top:1051px;width:214px">Donec iaculis maximus enim et tempor. Nullam bibendum quis nibh quis ullamcorper. Sed vehicula mollis elit at ultricies. Curabitur ligula ligula, faucibus vel pretium eget, aliquet eu orci. Proin sed efficitur orci.</p>
  <p class="byline" style="left:123px;top:1109px">By<span class="sep">|</span><b>February 26, 2015</b><span class="sep">|</span><b>Comments</b></p>
  <div class="stats" style="left:123px;top:1130px"><span><svg width="6" height="6"><use href="#i-like"/></svg>62</span><span><svg width="7" height="6"><use href="#i-view"/></svg>95</span><span><svg width="7" height="6"><use href="#i-comment"/></svg>12</span></div>

  <!-- bottom list -->
  <div class="media" role="img" aria-label="Guests at a premiere" style="left:346px;top:846px;width:50px;height:33px;background:linear-gradient(120deg,#9c8a7c,#3a3232)"></div>
  <p class="mini-item" style="left:399px;top:845px;width:76px">Lorem ipsum dolor sit am et, consectetur adi piscing elit. Fusce lorem metus.<time>February 26, 2015</time></p>
  <div class="rule" style="left:346px;top:884px;width:126px"></div>
  <div class="media" role="img" aria-label="Blonde actress portrait" style="left:346px;top:891px;width:50px;height:33px;background:linear-gradient(120deg,#b3c0cc,#d8b88a 60%,#8a98a6)"></div>
  <p class="mini-item" style="left:399px;top:890px;width:76px">Lorem ipsum dolor sit am et, consectetur adi piscing elit. Fusce lorem metus.<time>February 26, 2015</time></p>
  <div class="rule" style="left:346px;top:929px;width:126px"></div>
  <div class="media" role="img" aria-label="Actor smiling at an event" style="left:346px;top:936px;width:50px;height:33px;background:linear-gradient(120deg,#5a3a2c,#c79a7e 55%,#3a2a24)"></div>
  <p class="mini-item" style="left:399px;top:935px;width:76px">Lorem ipsum dolor sit am et, consectetur adi piscing elit. Fusce lorem metus.<time>February 26, 2015</time></p>
  <div class="rule" style="left:346px;top:974px;width:126px"></div>
  <div class="media" role="img" aria-label="Superhero film emblem" style="left:346px;top:981px;width:50px;height:33px;background:radial-gradient(circle,#6e2626,#1c1d20 70%)"></div>
  <p class="mini-item" style="left:399px;top:980px;width:76px">Lorem ipsum dolor sit am et, consectetur adi piscing elit. Fusce lorem metus.<time>February 26, 2015</time></p>
  <div class="rule" style="left:346px;top:1019px;width:126px"></div>
  <div class="media" role="img" aria-label="Actor in a suit on the phone" style="left:346px;top:1026px;width:50px;height:33px;background:linear-gradient(120deg,#8e8a86,#3f4248 60%)"></div>
  <p class="mini-item" style="left:399px;top:1025px;width:76px">Lorem ipsum dolor sit am et, consectetur adi piscing elit. Fusce lorem metus.<time>February 26, 2015</time></p>
  <div class="rule" style="left:346px;top:1064px;width:126px"></div>
  <div class="media" role="img" aria-label="Singer portrait" style="left:346px;top:1071px;width:50px;height:33px;background:linear-gradient(120deg,#ddd6d3,#4a3a38 50%,#a33a3a)"></div>
  <p class="mini-item" style="left:399px;top:1070px;width:76px">Lorem ipsum dolor sit am et, consectetur adi piscing elit. Fusce lorem metus.<time>February 26, 2015</time></p>
</main>

<aside>
  <div class="vrule" style="left:482px;top:60px;height:1096px"></div>

  <div class="media" role="img" aria-label="Actress in a red dress" style="left:488px;top:72px;width:48px;height:34px;background:linear-gradient(120deg,#6a4a52,#b82838 60%)"></div>
  <p class="mini-item" style="left:541px;top:71px;width:74px">Lorem ipsum dolor sit am et, consectetur adi piscing elit. Fusce lorem metus.<time>February 26, 2015</time></p>
  <div class="rule" style="left:485px;top:111px;width:129px"></div>
  <div class="media" role="img" aria-label="Blonde actress portrait" style="left:488px;top:116px;width:48px;height:34px;background:linear-gradient(120deg,#b3c0cc,#d8b88a 60%,#8a98a6)"></div>
  <p class="mini-item" style="left:541px;top:116px;width:74px">Lorem ipsum dolor sit am et, consectetur adi piscing elit. Fusce lorem metus.<time>February 26, 2015</time></p>
  <div class="rule" style="left:485px;top:156px;width:129px"></div>
  <div class="media" role="img" aria-label="Actor smiling at an event" style="left:488px;top:161px;width:48px;height:34px;background:linear-gradient(120deg,#5a3a2c,#c79a7e 55%,#3a2a24)"></div>
  <p class="mini-item" style="left:541px;top:161px;width:74px">Lorem ipsum dolor sit am et, consectetur adi piscing elit. Fusce lorem metus.<time>February 26, 2015</time></p>
  <div class="rule" style="left:485px;top:201px;width:129px"></div>
  <div class="media" role="img" aria-label="Actress holding an award trophy" style="left:488px;top:207px;width:48px;height:34px;background:linear-gradient(120deg,#d8c49a,#6a5030 60%,#c7a55a)"></div>
  <p class="mini-item" style="left:541px;top:206px;width:74px">Lorem ipsum dolor sit am et, consectetur adi piscing elit. Fusce lorem metus.<time>February 26, 2015</time></p>
  <div class="rule" style="left:485px;top:248px;width:129px"></div>

  <h3 class="widget-label" style="left:487px;top:256px">SEARCH</h3>
  <div class="field" style="left:487px;top:276px;width:99px;height:21px;border-radius:3px 0 0 3px"></div>
  <div class="search-btn" style="left:585px;top:276px;width:29px;height:21px"></div>
  <svg class="abs" style="left:593px;top:280px" width="13" height="13" viewBox="0 0 11 11"><circle cx="4.5" cy="4.5" r="3" fill="none" stroke="#fff" stroke-width="1.6"/><path d="M6.8 6.8l3 3" stroke="#fff" stroke-width="2"/></svg>
  <div class="rule" style="left:485px;top:310px;width:129px"></div>

  <h3 class="popular-title" style="left:487px;top:322px">MOST POPULAR</h3>
  <p class="popular-item" style="top:340px"><b>1</b>Lorem ipsum dolor sit amet, consecte<br>tur adipiscing elit.</p>
  <div class="rule" style="left:485px;top:363px;width:129px"></div>
  <p class="popular-item" style="top:369px"><b>2</b>Phasellus maximus, purus ac placerat<br>varius, arcu purus varius elit, eget.</p>
  <div class="rule" style="left:485px;top:393px;width:129px"></div>
  <p class="popular-item" style="top:398px"><b>3</b>Volutpat augue odio quis enim nulla<br>rhoncus urna id tortor fermentum...</p>
  <div class="rule" style="left:485px;top:422px;width:129px"></div>
  <p class="popular-item" style="top:428px"><b>4</b>Vestibulum sed eros nibh. Curabitur id<br>placerat augue. Sed blandit...</p>
  <div class="rule" style="left:485px;top:452px;width:129px"></div>
  <p class="popular-item" style="top:458px"><b>5</b>Consequat diam, dignissim ornare<br>metus tristique nec.</p>
  <div class="rule" style="left:485px;top:482px;width:129px"></div>
  <p class="popular-item" style="top:487px"><b>6</b>Consequat diam, dignissim ornare<br>metus tristique nec.</p>
  <div class="rule" style="left:485px;top:512px;width:129px"></div>

  <section class="follow-box">
    <h3>FOLLOW US</h3>
    <div class="social" style="left:8px;top:30px">
      <span><i></i>Pals</span><span><i></i>Feed</span><span><i></i>Chirp</span><span><i></i>Spot</span>
    </div>
  </section>

  <h3 class="categories-title" style="left:487px;top:610px">CATEGORIES</h3>
  <p class="category" style="top:632px">Lorem ipsum dolor<em>(24)</em></p>
  <div class="rule" style="left:485px;top:647px;width:129px"></div>
  <p class="category" style="top:656px">Phasellus maximus, purus<em>(22)</em></p>
  <div class="rule" style="left:485px;top:671px;width:129px"></div>
  <p class="category" style="top:680px">Volutpat augue odio<em>(20)</em></p>
  <div class="rule" style="left:485px;top:695px;width:129px"></div>
  <p class="category" style="top:704px">Vestibulum sed eros nibh<em>(18)</em></p>
  <div class="rule" style="left:485px;top:719px;width:129px"></div>
  <p class="category" style="top:728px">Consequat diam, dignissim<em>(16)</em></p>
  <div class="rule" style="left:485px;top:743px;width:129px"></div>
  <p class="category" style="top:752px">Vestibulum sed eros nibh<em>(14)</em></p>
  <div class="rule" style="left:485px;top:767px;width:129px"></div>
  <p class="category" style="top:776px">Consequat diam, dignissim<em>(12)</em></p>
  <div class="rule" style="left:485px;top:791px;width:129px"></div>
  <p class="category" style="top:800px">Consequat diam, dignissim<em>(10)</em></p>
  <div class="rule" style="left:485px;top:815px;width:129px"></div>
  <p class="category" style="top:824px">Consequat diam, dignissim<em>(8)</em></p>
  <div class="rule" style="left:485px;top:839px;width:129px"></div>

  <h3 class="section-title" style="left:487px;top:857px">Search</h3>
  <p class="newsletter-note" style="left:487px;top:871px">Get monthly fresh updates in your mailbox</p>
  <div class="field" style="left:487px;top:887px;width:127px;height:21px">Email Address</div>
  <div class="field" style="left:487px;top:917px;width:127px;height:21px">First Name</div>
  <div class="field" style="left:487px;top:947px;width:127px;height:21px">Last Name</div>
  <div class="subscribe">SUBSCRIBE</div>
</aside>

<footer class="site-footer">
  <p class="footer-about">Lorem ipsum dolor sit amet, consectetur adipiscing elit. Phasellus maximus, purus ac placerat varius, arcu purus varius elit</p>
  <nav class="footer-links">Mustreads | Cine | Music<br>Entertainment | Social Media | Features<small>Copyright © 2014</small></nav>
  <p class="footer-follow">FOLLOW US</p>
  <div class="footer-social"><span><i></i>Pals</span><span><i></i>Feed</span><span><i></i>Chirp</span><span><i></i>Spot</span></div>
</footer>

</body>
</html>
```